20 year old business card needs re-design

We need to redesign our corporate business card look. We need something that appears more modern, eye catchy but professional.

Target Market(s)

manufacturing industry

Industry/Entity Type

Manufacturer

Contact Information for Business Card

One side can have the logo. Other side can have contact information.

Font styles to use
Serif

Colors
3277b5
33b8a4
ffffff

Requirements
Must have
• Eye catchy - need to standout from the crowd. company logo cannot change. Full name, job title, phone number and email address.
Should not have
• Fax, business address is not necessary.

```html
<!DOCTYPE html>
<html lang="en">
<head>
<meta charset="utf-8">
<title>Norvale Industrial – Business Card</title>
<link rel="stylesheet" href="https://fonts.googleapis.com/css2?family=Arimo:wght@400;700&display=swap">
<style>
  :root {
    --brand-blue: #1f55b0;
    --brand-blue-deep: #16449a;
    --ink: #1c1c1c;
    --paper: #ffffff;
    --paper-shade: #eef0f2;
    --backdrop: #e4e6e9;
    --text-font: "Arimo", Arial, sans-serif;
  }
  * { box-sizing: border-box; margin: 0; padding: 0; }
  html, body {
    width: 1200px; height: 997px; overflow: hidden;
    background: var(--backdrop);
    font-family: var(--text-font);
  }
  .sheet {
    position: relative; width: 1200px; height: 997px;
    display: flex; align-items: center; justify-content: center; gap: 40px;
  }
  .card {
    position: relative; width: 520px; height: 297px;
    border-radius: 4px; overflow: hidden;
    box-shadow: 0 10px 28px rgba(0,0,0,.18);
  }

  /* Front: logo side */
  .card--front {
    background: linear-gradient(160deg, var(--brand-blue) 0%, var(--brand-blue-deep) 100%);
    display: flex; flex-direction: column; align-items: center; justify-content: center;
  }
  .front__name {
    color: var(--paper); font-weight: 700; font-size: 40px; letter-spacing: 1px;
    margin-bottom: 34px;
  }
  .front__web {
    background: var(--paper); color: var(--brand-blue);
    font-weight: 700; font-size: 17px; letter-spacing: .5px;
    padding: 7px 26px; border-radius: 20px;
  }

  /* Back: contact side */
  .card--back {
    background: linear-gradient(160deg, var(--paper) 0%, var(--paper-shade) 100%);
  }
  .back__tab {
    position: absolute; background: var(--brand-blue);
  }
  .back__tab--left { left: 0; top: 88px; bottom: 0; width: 14px; border-radius: 0 14px 0 0; }
  .back__tab--right { right: 0; top: 0; height: 168px; width: 14px; border-radius: 0 0 0 14px; }
  .back__name {
    position: absolute; top: 48px; left: 0; right: 0; text-align: center;
    color: var(--ink); font-weight: 700; font-size: 36px; letter-spacing: 1px;
  }
  .back__person {
    position: absolute; left: 70px; top: 196px; text-align: center;
  }
  .person__name { color: var(--brand-blue); font-weight: 700; font-size: 19px; letter-spacing: .3px; }
  .person__title { color: var(--ink); font-weight: 700; font-size: 14px; margin-top: 2px; }
  .back__divider {
    position: absolute; left: 268px; top: 160px; width: 2px; height: 84px;
    background: linear-gradient(to bottom, transparent, var(--brand-blue), transparent);
  }
  .back__contact {
    position: absolute; left: 296px; top: 154px;
    color: var(--ink); font-size: 13.5px; line-height: 17px;
  }
  .contact__address { margin-bottom: 8px; }
  .contact__line { display: flex; align-items: center; gap: 10px; margin-top: 4px; }
  .contact__icon { width: 16px; height: 16px; flex: none; }
</style>
</head>
<body>
<main class="sheet">
  <section class="card card--front" aria-label="Card front">
    <div class="front__name">NORVALE INDUSTRIAL</div>
    <div class="front__web">WWW.NORVALEINDUSTRIAL.COM</div>
  </section>

  <section class="card card--back" aria-label="Card back">
    <span class="back__tab back__tab--left"></span>
    <span class="back__tab back__tab--right"></span>
    <div class="back__name">NORVALE INDUSTRIAL</div>

    <div class="back__person">
      <div class="person__name">MAREN HOLT</div>
      <div class="person__title">Director</div>
    </div>

    <span class="back__divider"></span>

    <div class="back__contact">
      <div class="contact__address">412 Mill Line road 9<br>Ashford, ON K0A2B0</div>
      <div class="contact__line">
        <svg class="contact__icon" viewBox="0 0 16 16" aria-hidden="true">
          <circle cx="8" cy="8" r="8" fill="#1f55b0"/>
          <path d="M4 6.5c0-1 1.8-2 4-2s4 1 4 2l-1.4.6-.6-1.1H6l-.6 1.1z M5.2 8h5.6l.8 3.5H4.4z" fill="#fff"/>
        </svg>
        <span>0455208731</span>
      </div>
      <div class="contact__line">
        <svg class="contact__icon" viewBox="0 0 16 16" aria-hidden="true">
          <circle cx="8" cy="8" r="8" fill="#1f55b0"/>
          <rect x="4" y="5.2" width="8" height="5.6" fill="none" stroke="#fff" stroke-width="1"/>
          <path d="M4 5.4l4 3 4-3" fill="none" stroke="#fff" stroke-width="1"/>
        </svg>
        <span>maren@norvaleindustrial.com</span>
      </div>
    </div>
  </section>
</main>
</body>
</html>
```